2nd Opinion Radiology web page

Looking for a web page design for second opinion radiology service. Main page will have a link directing user to locate CD on their computer/device, and will take contents of CD and upload to server, which I will specify.

Web page needs a form to enter user's name, contact info, and create a log in for user. User must click to accept terms of service, which will be a paragraph which i will provide. User will log back in, after uploading cd, to find report, which will be able to be viewed once user pays, by coinvera. User will need to be able to download report.

There will be a small paragraph explaining what we do: Provide expert second opinions, worldwide. We provide interpretations from radiologists with many years of experience and training from the world's best institutions, including brennick and corvalen regional hospital.

A second paragraph: Have questions or doubts about your CT or MRI? Get a second opinion from experts at ScanPerch. Tap into the full potential of your images.

Thanks

Reason: The website does not need to be fully coded, however, should include graphics and design so a web designer can simply take the design, images, and objects and code the site.

People who are unsure of their medical care and looking for a second opinion.

Training

```html
<!DOCTYPE html>
<html lang="en">
<head>
<meta charset="utf-8">
<title>Second Opinion Radiology</title>
<link rel="stylesheet" href="https://fonts.googleapis.com/css2?family=Roboto:wght@300;400&display=swap">
<style>
  :root {
    --sky: #41b4f3;
    --sky-light: #82c8f3;
    --sky-deep: #3896cb;
    --steel: #949ea5;
    --ink: #2b2b2b;
    --brand-blue: #1a3fb3;
    --white: #ffffff;
  }
  * { box-sizing: border-box; margin: 0; padding: 0; }
  html, body { width: 1200px; height: 1196px; overflow: hidden; }
  body { position: relative; font-family: "Roboto", "Helvetica Neue", Arial, sans-serif; font-weight: 300; color: var(--ink); background: var(--white); }

  .site-header { position: absolute; left: 0; top: 0; width: 1200px; height: 141px; background: linear-gradient(#ffffff, #ebebeb); }
  .brand { position: absolute; left: 47px; top: 32px; display: flex; align-items: center; gap: 12px; }
  .brand-mark { width: 76px; height: 76px; border-radius: 50%; border: 2px solid #3a3a55; background: var(--white); }
  .brand-name { font-size: 28px; font-weight: 400; color: var(--brand-blue); letter-spacing: -0.3px; }
  .main-nav { position: absolute; top: 50px; left: 594px; height: 36px; }
  .main-nav a { position: absolute; top: 0; height: 36px; line-height: 36px; font-size: 23px; color: var(--sky); text-decoration: none; white-space: nowrap; }
  .main-nav .is-active { left: 0; width: 99px; text-align: center; background: linear-gradient(#ffffff, #ededed); border-radius: 4px; box-shadow: 0 1px 3px rgba(0,0,0,.3); }
  .nav-company { left: 144px; } .nav-services { left: 298px; } .nav-contact { left: 428px; }

  .top-band { position: absolute; left: 0; top: 141px; width: 1200px; height: 21px; background: var(--sky); }

  .hero { position: absolute; left: 0; top: 162px; width: 1200px; height: 381px; background: linear-gradient(#ffffff 55%, #f1f1f1); }
  .hero-photo { position: absolute; left: 170px; top: 5px; width: 322px; height: 397px; background: linear-gradient(#e8ecef, #d5dce2); border-radius: 120px 120px 0 0; }
  .hero-kicker { position: absolute; left: 522px; top: 86px; font-size: 28px; }
  .hero-title { position: absolute; left: 522px; top: 124px; font-size: 46px; font-weight: 300; line-height: 48px; }
  .locate-btn { position: absolute; left: 523px; top: 240px; width: 314px; height: 74px; background: var(--sky); color: var(--white); font-size: 39px; padding-left: 20px; line-height: 74px; text-decoration: none; }
  .locate-btn svg { position: absolute; left: 232px; top: 11px; }

  .soft-band { position: absolute; left: 0; top: 543px; width: 1200px; height: 21px; background: var(--sky-light); }
  .photo-foot { position: absolute; left: 207px; top: 543px; width: 183px; height: 21px; background: #9fd2f1; }
  .blue-panel { position: absolute; left: 0; top: 564px; width: 1200px; height: 351px; background: var(--sky); }
  .steel-band { position: absolute; left: 0; top: 915px; width: 1200px; height: 64px; background: var(--steel); }

  .welcome { position: absolute; left: 90px; top: 586px; width: 432px; height: 393px; background: var(--white); border-radius: 5px 5px 0 0; padding: 22px 20px 0 20px; }
  .welcome h2 { font-size: 30px; font-weight: 300; margin-bottom: 14px; }
  .welcome p { font-size: 15px; line-height: 26px; text-align: justify; margin-bottom: 20px; }

  .register-title { position: absolute; left: 560px; top: 584px; font-size: 30px; color: var(--white); }
  .field { position: absolute; width: 292px; height: 51px; border-radius: 4px; background: var(--white); font-size: 21px; color: var(--sky); padding-left: 17px; line-height: 51px; }
  .terms { position: absolute; left: 566px; top: 854px; display: flex; align-items: center; gap: 14px; font-size: 23px; color: var(--white); }
  .terms .box { width: 32px; height: 32px; background: var(--white); }
  .terms strong { font-weight: 300; color: #111; }
  .submit-btn { position: absolute; left: 783px; top: 921px; width: 124px; height: 51px; background: var(--white); border-radius: 4px; color: var(--sky); font-size: 21px; text-align: center; line-height: 51px; }

  .site-footer { position: absolute; left: 0; top: 1117px; width: 1200px; height: 79px; background: var(--sky-deep); }
  .footer-links { position: absolute; right: 25px; top: 10px; font-size: 18px; color: var(--white); }
</style>
</head>
<body>
  <header class="site-header">
    <div class="brand"><span class="brand-mark"></span><span class="brand-name">companyname</span></div>
    <nav class="main-nav">
      <a class="is-active" href="#">home</a>
      <a class="nav-company" href="#">company</a>
      <a class="nav-services" href="#">services</a>
      <a class="nav-contact" href="#">contact us</a>
    </nav>
  </header>
  <div class="top-band"></div>

  <section class="hero">
    <div class="hero-photo" role="img" aria-label="Smiling doctor in a white coat with a stethoscope, writing on a tablet"></div>
    <p class="hero-kicker">Have questions or doubts about your CT or MRI?</p>
    <h1 class="hero-title">Get a second opinion from<br>the experts</h1>
    <a class="locate-btn" href="#">LOCATE CD
      <svg width="52" height="52" viewBox="0 0 52 52"><circle cx="26" cy="26" r="26" fill="#fff"/><circle cx="26" cy="26" r="16" fill="#e6e6e6"/><circle cx="26" cy="26" r="8" fill="#41b4f3"/></svg>
    </a>
  </section>

  <div class="soft-band"></div>
  <div class="photo-foot"></div>
  <div class="blue-panel"></div>
  <div class="steel-band"></div>

  <article class="welcome">
    <h2>Welcome</h2>
    <p>Lorem ipsum dolor sit amet, consectetur adipisicing elit, sed do eiusmod tempor incididunt ut labore et dolore magna aliqua. Ut enim ad minim veniam.</p>
    <p>Lorem ipsum dolor sit amet, consectetur adipisicing elit, sed do eiusmod tempor incididunt ut labore et dolore magna aliqua. Ut enim ad minim veniam.</p>
  </article>

  <h2 class="register-title">Register Here</h2>
  <div class="field" style="left:559px;top:631px">Firstname</div>
  <div class="field" style="left:877px;top:631px">Lastname</div>
  <div class="field" style="left:559px;top:705px">Email</div>
  <div class="field" style="left:879px;top:703px">Username</div>
  <div class="field" style="left:561px;top:784px">Mobile No.</div>
  <div class="field" style="left:879px;top:782px">Password</div>
  <div class="terms"><span class="box"></span><span>Check if you agree to the <strong>Terms and Agreements</strong></span></div>
  <div class="submit-btn">Submit</div>

  <footer class="site-footer">
    <p class="footer-links">Privacy Policy | Terms | Copyright | Contact Us</p>
  </footer>
</body>
</html>
```